Educational Software Company Needs Banner Ads Prompting an Event

We are looking for a series of banner ads (to be used in conjunction with plexa adlink), pushing people to register for our upcoming road tour, Hallway Heroes. Hallway Heroes is a series of one-day workshops that offer best practices for individuals in the educational operations industry. To learn more about the event please view the website at: hallwayheroes.gradefinch.com.

Feel free to use any of the language from the website, logo (attached), and the hex colors which are listed in the "must have" section below.

Some language that we have use on other marketing materials:
"We're Hitting the Road!"
Our 2014 road tour is heading to a city near you!
"Invest in Your Success"
"We're Hitting the Road, and Heading Your Way!"
"Hallway Heroes - A free, one-day workshop offering lessons for success"
"Seating is Limited - Register Today!"

Supported ad sizes and specs:
250 x 250 square
200 x 200 square
468 x 60 banner
728 x 90 leaderboard
300 x 250 inline rectangle
120 x 600 skyscraper
160 x 600 wide skyscrapper
320 x 50 mobile leaderboard

The call to action for the ad should be to "Register Today!"

Target Market(s)

educational operations professionals, i.e. maintenance directors, energy managers, superintendents, business officers etc...

Industry/Entity Type

Marketing

Requirements
Must have
• event logo and/or event name using event colors; CTA button reading "Register Today!"

Colors:
HH – Red #A63515
R: 166
G: 53
B: 21

HH – Dark Gray #726658
R: 114
G: 102
B: 88

HH – Light Gray #CECECE
R: 206
G: 206
B: 206

HH – Orange #EDA45B
R: 237
G: 164
B: 91
Nice to have
• Consider using list of stops on larger banner ads.

1/14/2014 Seattle, CA
1/16/2014 Phoenix, CA
1/21/2014 Sacramento, CA
1/23/2014 Ontario, CA
2/13/2014 Kilgore, TX
2/11/2014 Coppell, TX
TBD Schaumburg, IL

```html
<!DOCTYPE html>
<html lang="en">
<head>
<meta charset="utf-8">
<title>Hallway Heroes – Banner Ads</title>
<link href="https://fonts.googleapis.com/css2?family=Bitter:wght@400;600;700&display=swap" rel="stylesheet">
<style>
  :root{
    --hh-red:#a63515;
    --hh-badge:#98301a;
    --hh-dark-gray:#726658;
    --hh-light-gray:#cecece;
    --hh-orange:#eda45b;
    --sky:#a9dcdc;
    --paper:#ffffff;
    --paper-shade:#ececec;
    --stage:#000000;
  }
  *{margin:0;padding:0;box-sizing:border-box}
  html,body{width:1200px;height:623px;overflow:hidden;background:var(--stage)}
  body{font-family:"Bitter",Georgia,serif;color:var(--hh-red)}
  .board{position:absolute;left:0;top:0;width:1189px;height:617px;transform-origin:0 0;transform:scale(1.0093,1.0097)}
  .ad{position:absolute;overflow:hidden;background:var(--sky)}
  .ad-bg{position:absolute;inset:0;width:100%;height:100%}
  .abs{position:absolute}
  .event-name{position:absolute;font-weight:700;color:var(--hh-red);text-align:center;line-height:1.05;letter-spacing:.02em;text-transform:uppercase}
  .tagline{position:absolute;color:var(--hh-red);line-height:1.1}
  .tagline strong{font-weight:700}
  .dest-title{position:absolute;color:var(--hh-dark-gray);font-weight:600;letter-spacing:.03em}
  .stops{position:absolute;list-style:none;color:var(--hh-red);font-weight:600}
  .cta{position:absolute;border-radius:50%;background:var(--hh-badge);
       border:2px dotted #c4573a;box-shadow:0 0 0 2px var(--hh-badge);
       display:flex;align-items:center;justify-content:center;text-align:center;
       color:var(--hh-orange);line-height:1.15;text-decoration:none}
  .scene{position:absolute;background:linear-gradient(180deg,#a9dcdc 0%,#a9dcdc 35%,#7fa58a 55%,#8b9e5c 75%,#6e6a5c 100%)}

  /* skyscraper */
  .sky{left:155px;top:13px;width:158px;height:591px}
  .sky .event-name{left:0;width:158px;top:70px;font-size:22px}
  .sky .tagline{left:0;width:158px;top:153px;text-align:center;font-size:20px}
  .sky .cta{left:193px;top:0}
  .sky .dest-title{left:0;width:158px;top:358px;text-align:center;font-size:17px}
  .sky .stops{left:0;width:158px;top:382px;text-align:center;font-size:17px;line-height:19.6px}
  .sky .scene{left:0;top:503px;width:158px;height:88px}

  /* leaderboard */
  .leader{left:323px;top:54px;width:715px;height:88px}
  .leader .event-name{left:10px;top:29px;width:62px;font-size:12px}
  .leader .tagline{left:90px;top:30px;font-size:16px;line-height:19px}
  .leader .dest-title{left:322px;top:9px;font-size:17px}
  .leader .stops{left:322px;top:33px;font-size:13px;line-height:16px}
  .leader .scene{left:575px;top:0;width:140px;height:88px}

  /* inline rectangle */
  .rect{left:323px;top:162px;width:295px;height:246px}
  .rect .event-name{left:18px;top:50px;width:100px;font-size:17px}
  .rect .tagline{left:10px;top:145px;font-size:17.5px;line-height:20.5px}
  .rect .dest-title{right:25px;top:14px;font-size:17px}
  .rect .stops{right:25px;top:40px;text-align:right;font-size:13px;line-height:15.2px}
  .rect .scene{left:128px;top:140px;width:167px;height:106px;clip-path:polygon(40% 0,100% 0,100% 100%,0 100%)}
</style>
</head>
<body>
<main class="board">

  <!-- Skyscraper 160 x 600 -->
  <section class="ad sky" aria-label="Skyscraper ad">
    <svg class="ad-bg" viewBox="0 0 158 591" preserveAspectRatio="none" aria-hidden="true">
      <defs>
        <linearGradient id="skyPaper" x1="0" y1="0" x2="0" y2="1">
          <stop offset="0" stop-color="var(--paper-shade)"/>
          <stop offset=".3" stop-color="var(--paper)"/>
        </linearGradient>
      </defs>
      <polygon points="0,0 158,0 158,282 79,318 0,282" fill="url(#skyPaper)"/>
    </svg>
    <div class="event-name">Hallway<br>Heroes</div>
    <p class="tagline">A free,<br><strong>one-day</strong><br>workshop for<br>operations<br>professionals</p>
    <a class="cta" href="#" style="left:39px;top:276px;width:70px;height:70px;font-size:14px">Register<br>Today!</a>
    <h3 class="dest-title">DESTINATION</h3>
    <ul class="stops">
      <li>Seattle, CA</li><li>Phoenix, CA</li><li>Sacramento, CA</li>
      <li>Ontario, CA</li><li>Kilgore, TX</li><li>Coppell, TX</li>
    </ul>
    <div class="scene" role="img" aria-label="Illustration of a red station wagon with luggage on the roof driving past green mountains"></div>
  </section>

  <!-- Leaderboard 728 x 90 -->
  <section class="ad leader" aria-label="Leaderboard ad">
    <svg class="ad-bg" viewBox="0 0 715 88" preserveAspectRatio="none" aria-hidden="true">
      <defs>
        <linearGradient id="leadPaper" x1="0" y1="0" x2="1" y2="0">
          <stop offset="0" stop-color="var(--paper)"/>
          <stop offset="1" stop-color="var(--paper-shade)"/>
        </linearGradient>
      </defs>
      <polygon points="0,0 530,0 560,88 0,88" fill="url(#leadPaper)"/>
    </svg>
    <div class="event-name">Hallway<br>Heroes</div>
    <p class="tagline">A free,&nbsp; <strong>one-day</strong> workshop<br>for operations professionals</p>
    <h3 class="dest-title">DESTINATION</h3>
    <ul class="stops">
      <li>Seattle, CA | Phoenix, CA</li>
      <li>Sacramento, CA | Ontario, CA</li>
      <li>Kilgore, TX | Coppell, TX</li>
    </ul>
    <div class="scene" role="img" aria-label="Illustration of a red station wagon with luggage on the roof driving past green mountains"></div>
    <a class="cta" href="#" style="left:512px;top:11px;width:64px;height:64px;font-size:13.5px">Register<br>Today!</a>
  </section>

  <!-- Inline rectangle 300 x 250 -->
  <section class="ad rect" aria-label="Inline rectangle ad">
    <svg class="ad-bg" viewBox="0 0 295 246" preserveAspectRatio="none" aria-hidden="true">
      <defs>
        <linearGradient id="rectPaper" x1="0" y1="0" x2="1" y2="1">
          <stop offset="0" stop-color="var(--paper-shade)"/>
          <stop offset=".5" stop-color="var(--paper)"/>
        </linearGradient>
      </defs>
      <polygon points="0,0 128,0 160,140 128,246 0,246" fill="url(#rectPaper)"/>
    </svg>
    <div class="event-name">Hallway<br>Heroes</div>
    <h3 class="dest-title">DESTINATION</h3>
    <ul class="stops">
      <li>Seattle, CA</li><li>Phoenix, CA</li><li>Sacramento, CA</li>
      <li>Ontario, CA</li><li>Kilgore, TX</li><li>Coppell, TX</li>
    </ul>
    <div class="scene" role="img" aria-label="Illustration of a red station wagon with luggage on the roof driving past green mountains"></div>
    <a class="cta" href="#" style="left:116px;top:80px;width:68px;height:68px;font-size:14px">Register<br>Today!</a>
    <p class="tagline">A free, <strong>one-day</strong><br>workshop for<br>operations<br>professionals</p>
  </section>

</main>
</body>
</html>
```